Tarn Bites menu + business card design

I want a menu design for my Food Truck.

I have attached the logo for it and my sliders will have different colors such as ( Black sliders, Red sliders and normal color) a picture will illustrates what I mean.

The menu should include:

Sliders:

Tarn Bite Single

Tarn Bites Meal

Fries:

Tarn Fries

Drinks:
Tarn Mojito

Water

VelaFizz

Desserts:

Charcoal cake

Target Market(s)

All

Industry/Entity Type

Business

Contact Information for Business Card

My theme is black and yellow like my logo

Colors

Designer to choose colors to be used in the design.

Requirements
Must have
• WhatsApp logo and the number for it is : +966500473829 " please dont squeeze the numbers".
• Instagram logo and my account is: TarnBites
• Snapchat logo and my account is: TarnBites
• Email logo and my email is: TheTarnBites@postvale.com
Nice to have
• Circle design of the whole business card but it is not a must
• i will attach a picture.

```html
<!DOCTYPE html>
<html lang="en">
<head>
<meta charset="utf-8">
<title>Tarn Bites – Business Card</title>
<link href="https://fonts.googleapis.com/css2?family=Fredoka:wght@500;600&display=swap" rel="stylesheet">
<style>
  :root{
    --page:#e6e6e6;
    --card:#f7a51d;
    --card-deep:#f29a18;
    --card-light:#fab63a;
    --ink:#ffffff;
    --brand-ink:#1d1d1b;
  }
  *{margin:0;padding:0;box-sizing:border-box}
  html,body{width:1200px;height:798px;overflow:hidden}
  body{background:var(--page);font-family:"Fredoka",sans-serif;position:relative}
  .card{position:absolute;border-radius:50%}
  .card-front{left:74px;top:94px;width:572px;height:572px;
    background:radial-gradient(circle at 50% 50%,var(--card-light) 0%,var(--card) 50%,var(--card-deep) 100%)}
  .card-back{left:536px;top:122px;width:576px;height:576px;
    background:radial-gradient(circle at 50% 40%,var(--card-light) 0%,var(--card) 55%,var(--card) 100%);
    box-shadow:-6px 0 14px rgba(0,0,0,.12)}
  .dot-ring{position:absolute;inset:0;width:100%;height:100%}
  .brand-name{position:absolute;left:0;right:0;text-align:center;font-weight:600;color:var(--brand-ink);line-height:1}
  .card-front .brand-name{top:256px;font-size:66px}
  .card-back .brand-name{top:52px;font-size:30px}
  .contact{position:absolute;left:0;right:0;text-align:center;color:var(--ink);font-weight:600;line-height:1}
  .holder-name{top:134px;font-size:54px;letter-spacing:1px}
  .holder-role{top:182px;font-size:27px;left:-30px}
  .icon{position:absolute;left:50%;transform:translateX(-50%)}
  .icon-phone{top:238px}
  .phone-number{top:278px;font-size:31px;letter-spacing:1px}
  .social-icons{position:absolute;top:320px;left:0;right:0;display:flex;justify-content:center;gap:22px}
  .social-handle{top:360px;font-size:30px}
  .icon-mail{top:402px}
  .email{top:448px;font-size:25px}
</style>
</head>
<body>
  <div class="card card-front" role="img" aria-label="Orange card face with a soft sunburst glow behind the brand name">
    <div class="brand-name">Tarn Bites</div>
  </div>

  <div class="card card-back">
    <svg class="dot-ring" viewBox="0 0 576 576" aria-hidden="true">
      <circle cx="288" cy="288" r="274" fill="none" stroke="#fff" stroke-width="8"
              stroke-linecap="round" pathLength="100" stroke-dasharray="0 1"/>
    </svg>
    <div class="brand-name">Tarn Bites</div>
    <div class="contact holder-name">JOHN DOE</div>
    <div class="contact holder-role">POSITION</div>

    <svg class="icon icon-phone" width="38" height="38" viewBox="0 0 24 24" aria-label="Phone">
      <path d="M6.6 10.8a15 15 0 0 0 6.6 6.6l2.2-2.2a1 1 0 0 1 1-.25 11.4 11.4 0 0 0 3.6.57 1 1 0 0 1 1 1V20a1 1 0 0 1-1 1A17 17 0 0 1 3 4a1 1 0 0 1 1-1h3.5a1 1 0 0 1 1 1c0 1.25.2 2.45.57 3.57a1 1 0 0 1-.25 1z" fill="none" stroke="#fff" stroke-width="1.8" stroke-linejoin="round"/>
    </svg>
    <div class="contact phone-number">+966500473829</div>

    <div class="social-icons" aria-hidden="true">
      <svg width="36" height="36" viewBox="0 0 36 36"><circle cx="18" cy="18" r="15" fill="none" stroke="#fff" stroke-width="3"/></svg>
      <svg width="36" height="36" viewBox="0 0 36 36"><circle cx="18" cy="18" r="15" fill="none" stroke="#fff" stroke-width="3"/></svg>
    </div>
    <div class="contact social-handle">@TARNBITES</div>

    <svg class="icon icon-mail" width="48" height="34" viewBox="0 0 48 34" aria-label="Email">
      <rect x="2" y="2" width="44" height="30" fill="none" stroke="#fff" stroke-width="3" stroke-linejoin="round"/>
      <path d="M2 2l22 17L46 2M2 32l16-14M46 32L30 18" fill="none" stroke="#fff" stroke-width="3" stroke-linejoin="round"/>
    </svg>
    <div class="contact email">THETARNBITES@POSTVALE.COM</div>
  </div>
</body>
</html>
```